An innovative casting business is looking for a creative new packaging design. We create castings fo

We need a new creative packaging design for our creative castings. The packaging we used to have been similar to a tippy basket box with a handle. We used to use different materials (Wax) so it was very light and efficient. However now we are using stone so will need a brand new design and concept.
The final design should not be childish. We cater for all ages, it should be playful without being to over-sauced. We are looking for something creative and innovative and practical while also having a bit of a wow factor.

We do have a few ideas however would like to leave the door open. We are incredibly excited to see what everyone comes up with. By typing 'creative packaging' into google may bring some ideas...

Target Market(s)

Familes, Couples, Children, Keepsakes

Industry/Entity Type

Business

Requirements
Must have
• Must be innovative and creative.
Nice to have
• I would like to have the hand sit inside of something. This would be nice to have as it will stabilise the hand(s) for travel. I want to have something innovative and new. We have had the tippy basket type box before so would like to have something different. Its not important for it to have a handle.
Should not have
• Should not be childish

```html
<!DOCTYPE html>
<html lang="en">
<head>
<meta charset="utf-8">
<title>Corvel Casting – Box Packaging</title>
<link href="https://fonts.googleapis.com/css2?family=Source+Sans+3:wght@400&display=swap" rel="stylesheet">
<style>
  :root {
    --navy: #1c2d44;
    --navy-light: #30496a;
    --gold: #97805f;
    --gold-line: #b39c6e;
    --ink: #111111;
    --paper: #ffffff;
  }
  html, body {
    margin: 0;
    padding: 0;
    overflow: hidden;
  }
  .canvas {
    position: relative;
    width: 1200px;
    height: 1200px;
    background: var(--paper);
    font-family: "Source Sans 3", sans-serif;
    overflow: hidden;
  }
  .panel {
    position: absolute;
    background: var(--navy);
  }
  .side-lid   { left: 332px; top: 110px; width: 540px; height: 337px; }
  .side-band  { position: absolute; left: 348px; top: 449px; width: 508px; height: 7px; background: var(--gold); }
  .side-base  { left: 332px; top: 457px; width: 540px; height: 218px; }
  .top-lid    { left: 327px; top: 749px; width: 540px; height: 304px; }

  .brand-label {
    position: absolute;
    left: 522px;
    top: 255px;
    width: 159px;
    height: 131px;
    border: 1px solid var(--gold-line);
    background: linear-gradient(100deg, var(--navy) 0%, var(--navy-light) 100%);
    display: flex;
    align-items: center;
    justify-content: center;
    gap: 6px;
  }
  .brand-label .mark {
    width: 8px;
    height: 8px;
    background: var(--gold-line);
  }
  .brand-label .name {
    color: var(--gold-line);
    font-size: 15px;
    font-weight: 400;
    white-space: nowrap;
  }

  .top-name {
    position: absolute;
    left: 327px;
    top: 888px;
    width: 540px;
    text-align: center;
    color: var(--gold);
    font-size: 19px;
    font-weight: 400;
    letter-spacing: 0.2px;
  }

  .caption {
    position: absolute;
    width: 400px;
    text-align: center;
    color: var(--ink);
    font-size: 19px;
    font-weight: 400;
  }
  .caption-side { left: 394px; top: 689px; }
  .caption-top  { left: 394px; top: 1065px; }
</style>
</head>
<body>
  <div class="canvas">
    <div class="panel side-lid"></div>
    <div class="brand-label">
      <span class="mark"></span>
      <span class="name">Corvel Casting</span>
    </div>
    <div class="side-band"></div>
    <div class="panel side-base"></div>
    <p class="caption caption-side" style="margin:0">Side view of the box</p>

    <div class="panel top-lid"></div>
    <p class="top-name" style="margin:0">Corvel Casting</p>
    <p class="caption caption-top" style="margin:0">Top view of the box</p>
  </div>
</body>
</html>
```